Business Card Design

Online clothing womens clothing store, I sell my clothing online and at the markets.

i would like the attached picture on the front of the card and the contact information on the back.

Industry/Entity Type

Business

Contact Information for Business Card

Harbor Thistle
Maren Pilcott
(Instagram symbol) _harbor_thistle_
(Facebook symbol) www.facebook.com/harborthistleau/

W : www.harborthistle.com.au
E : info@harborthistle.com.au
P : 0478614203

```html
<!DOCTYPE html>
<html lang="en">
<head>
<meta charset="utf-8">
<title>Harbor Thistle – Business Card</title>
<link href="https://fonts.googleapis.com/css2?family=Dosis:wght@300;400&family=Open+Sans:wght@400&display=swap" rel="stylesheet">
<style>
  :root {
    --stage: #e9e6e1;
    --card-black: #0c0c0c;
    --card-grey: #3a3a3a;
    --swoosh: #ffffff;
    --ink-light: #f2f2f2;
    --ink-soft: #cfcfcf;
    --photo-top: #b9bdb1;
    --photo-mid: #9fa28c;
    --photo-low: #c9c2b0;
  }
  * { box-sizing: border-box; margin: 0; padding: 0; }
  html, body { width: 1200px; height: 858px; overflow: hidden; background: var(--stage); }
  .stage { position: relative; width: 1200px; height: 858px; }
  .card {
    position: absolute; left: 270px; width: 660px; height: 378px;
    overflow: hidden; border-radius: 4px;
    box-shadow: 0 10px 24px rgba(0,0,0,.25);
    background: var(--card-black);
  }
  .card--back { top: 30px; }
  .card--front { top: 450px; }
  .card svg.card-art { position: absolute; inset: 0; width: 100%; height: 100%; }

  .brand {
    position: absolute; font-family: "Dosis", sans-serif; font-weight: 300;
    color: var(--ink-light); letter-spacing: .32em; text-transform: uppercase;
    white-space: nowrap; line-height: 1;
  }
  .card--back .brand { left: 44px; top: 46px; font-size: 34px; }
  .owner {
    position: absolute; left: 150px; top: 100px;
    font-family: "Open Sans", sans-serif; font-size: 20px; letter-spacing: .14em;
    color: var(--ink-soft); line-height: 1.2;
  }
  .contacts {
    position: absolute; right: 28px; top: 140px; list-style: none;
    font-family: "Open Sans", sans-serif; font-size: 14px; color: var(--ink-light);
  }
  .contacts li { display: flex; justify-content: flex-end; align-items: center; gap: 10px; height: 22px; }
  .contacts .icon { width: 13px; height: 13px; background: var(--ink-light); border-radius: 2px; display: inline-block; flex: none; }

  .card--front .brand { left: 40px; top: 318px; font-size: 30px; }
</style>
</head>
<body>
<main class="stage">

  <section class="card card--back" aria-label="Business card, contact side">
    <svg class="card-art" viewBox="0 0 660 378" preserveAspectRatio="none" aria-hidden="true">
      <rect width="660" height="378" fill="var(--card-black)"/>
      <path d="M0,322 C200,346 460,332 660,298 L660,378 L0,378 Z" fill="var(--card-grey)"/>
      <path d="M0,262 C120,312 440,312 660,282 L660,290 C440,324 180,332 0,316 Z" fill="var(--swoosh)"/>
    </svg>
    <div class="brand">Harbor Thistle</div>
    <div class="owner">Maren Pilcott</div>
    <ul class="contacts">
      <li>0478614203
        <svg class="icon" viewBox="0 0 13 13"><path d="M3,2 L5,2 L6,4.5 L4.8,5.5 Q6,8 7.5,8.2 L8.5,7 L11,8 L11,10 Q6,11 3,5 Z" fill="#0c0c0c"/></svg>
      </li>
      <li>info@harborthistle.com.au
        <svg class="icon" viewBox="0 0 13 13"><rect x="2.5" y="3.5" width="8" height="6" fill="none" stroke="#0c0c0c"/><path d="M2.5,3.5 L6.5,7 L10.5,3.5" fill="none" stroke="#0c0c0c"/></svg>
      </li>
      <li>www.harborthistle.com.au
        <svg class="icon" viewBox="0 0 13 13"><circle cx="6.5" cy="6.5" r="4" fill="none" stroke="#0c0c0c"/><path d="M2.5,6.5 H10.5 M6.5,2.5 V10.5" stroke="#0c0c0c"/></svg>
      </li>
      <li>harborthistleau <span class="icon"></span></li>
      <li>harbor_thistle <span class="icon"></span></li>
    </ul>
  </section>

  <section class="card card--front" aria-label="Business card, photo side">
    <svg class="card-art" viewBox="0 0 660 378" preserveAspectRatio="none">
      <defs>
        <linearGradient id="photoTone" x1="0" y1="0" x2="0" y2="1">
          <stop offset="0" stop-color="var(--photo-top)"/>
          <stop offset=".55" stop-color="var(--photo-mid)"/>
          <stop offset="1" stop-color="var(--photo-low)"/>
        </linearGradient>
      </defs>
      <rect width="660" height="378" fill="var(--card-black)"/>
      <path d="M0,268 C220,296 470,276 660,176 L660,378 L0,378 Z" fill="var(--card-grey)"/>
      <path d="M0,260 C220,288 470,268 660,168 L660,173 C470,276 220,296 0,265 Z" fill="var(--swoosh)"/>
      <path d="M0,0 H660 V90 C560,200 330,240 0,215 Z" fill="url(#photoTone)" role="img" aria-label="Photograph of a woman in a black dress walking along a bush track"/>
    </svg>
    <div class="brand">Harbor Thistle</div>
  </section>

</main>
</body>
</html>
```